Gentlemen lifestyle blog in need of a logo and webdesign

Tallbrook is a site all about tests and reviews of products for gentlemen (Gin, whiskey, barber products, outdoor equipment, tobacco, coffe and more). It will be about fashion and a luxury lifestyle, health and fitness.
it will also include a online store

```html
<!DOCTYPE html>
<html lang="en">
<head>
<meta charset="utf-8">
<title>Tallbrook — Gentlemen's Lifestyle</title>
<link href="https://fonts.googleapis.com/css2?family=Cormorant+Garamond:wght@400;500;600&family=Montserrat:wght@400;500;600;700&display=swap" rel="stylesheet">
<style>
:root{
  --ink:#111111;
  --muted:#333333;
  --line:#d9d9d9;
  --band:#f2f2f2;
  --paper:#ffffff;
  --serif:'Cormorant Garamond', Georgia, serif;
  --sans:'Montserrat', Arial, sans-serif;
}
*{margin:0;padding:0;box-sizing:border-box}
html,body{width:1200px;height:5111px;overflow:hidden;background:var(--paper);color:var(--ink)}
body{position:relative;font-family:var(--sans)}
.abs{position:absolute}
.photo{position:absolute;display:block}
.btn-outline{position:absolute;border:2px solid var(--ink);font:500 13px/1 var(--sans);display:flex;align-items:center;justify-content:center;text-transform:uppercase;letter-spacing:.3px;background:transparent}
.btn-solid{position:absolute;background:var(--ink);color:#fff;font:600 14px/1 var(--sans);display:flex;align-items:center;justify-content:center;text-transform:uppercase}
.kicker{font:500 13px/1 var(--sans);text-transform:uppercase;letter-spacing:.3px}
.headline{font:400 35px/37px var(--serif)}
.lede{font:400 13.5px/21px var(--sans)}
.section-title{font:400 28px/1 var(--serif);text-transform:uppercase;letter-spacing:1px}
.tabs{position:absolute;display:flex;gap:46px;font:500 16px/1 var(--sans)}
.rule{position:absolute;left:70px;width:1051px;height:2px;background:var(--line)}
.card{position:absolute;border:1.5px solid #8a8a8a;background:#fff;overflow:hidden}
.card .photo{left:0;top:0;width:100%}
.mini-title{position:absolute;left:20px;font:500 17px/21px var(--serif)}
.rec-title{position:absolute;font:400 27px/33px var(--serif)}
.product-label{position:absolute;width:196px;text-align:center;font:600 14px/21px var(--sans);text-transform:uppercase}
.field{position:absolute;left:673px;width:432px;height:54px;background:#fff;font:400 14px/54px var(--sans);padding-left:16px;color:var(--ink)}
.footer-nav{position:absolute;left:68px;top:5001px;display:flex;gap:39px;font:500 14px/1 var(--sans);color:#fff;text-transform:uppercase}
.social{position:absolute;top:4980px;width:32px;height:32px;border:2px solid #fff;border-radius:50%}
</style>
</head>
<body>

<!-- Header -->
<header>
  <div class="btn-solid" style="left:70px;top:28px;width:103px;height:35px;font-size:12px">Shop now</div>
  <div class="abs" style="left:0;width:1200px;top:26px;text-align:center;font:500 31px/1 var(--serif);letter-spacing:1px;text-transform:uppercase">Tallbrook</div>
  <svg class="abs" style="left:1040px;top:32px" width="26" height="26" viewBox="0 0 26 26" fill="none" stroke="#111" stroke-width="2.2"><circle cx="11" cy="11" r="8.5"/><line x1="17.2" y1="17.2" x2="24" y2="24"/></svg>
  <svg class="abs" style="left:1094px;top:34px" width="26" height="20" viewBox="0 0 26 20" stroke="#111" stroke-width="3"><line x1="0" y1="2" x2="26" y2="2"/><line x1="0" y1="10" x2="26" y2="10"/><line x1="0" y1="18" x2="26" y2="18"/></svg>
</header>

<!-- Hero -->
<section class="hero">
  <div class="photo" role="img" aria-label="Smiling hiker with a red backpack resting on a mountain ridge, holding a bottle" style="left:0;top:85px;width:1200px;height:560px;background:linear-gradient(90deg,#f4f3ee 0%,#eeede4 40%,#cfc9b6 62%,#8b8371 80%,#6f7f58 100%)"><div style="position:absolute;left:0;bottom:0;width:100%;height:110px;background:linear-gradient(180deg,rgba(120,120,80,0),#6d6a3e)"></div></div>
  <div class="abs kicker" style="left:70px;top:216px">Latest article</div>
  <h1 class="abs headline" style="left:70px;top:246px;width:440px;font-weight:400">Lorem ipsum dolor sit amet, consectetur adipiscing elit, sed do eiusmod tempo.</h1>
  <p class="abs lede" style="left:70px;top:380px;width:360px">Lorem ipsum dolor sit amet, consectetur adi pisc ing elit, sed do eiusmod tempo.</p>
  <div class="btn-outline" style="left:70px;top:458px;width:144px;height:46px">Read more</div>
</section>

<!-- Editor's picks -->
<section class="editors-picks">
  <h2 class="abs section-title" style="left:70px;top:742px">Editor's picks</h2>
  <nav class="tabs" style="left:572px;top:747px"><span>All</span><span>Fashion</span><span>Luxury Lifestyle</span><span>Health</span><span>Fitness</span></nav>
  <div class="rule" style="top:797px"></div>

  <article class="card" style="left:70px;top:823px;width:515px;height:570px">
    <div class="photo" role="img" aria-label="Smiling bearded man in a beanie holding a coffee cup outdoors" style="height:301px;background:linear-gradient(135deg,#5c5a55,#9a8c7c 55%,#c9b8a2)"></div>
    <p class="abs" style="left:38px;top:345px;width:440px;font:400 25px/31px var(--serif)">Lorem ipsum dolor sit amet, consectetur adipiscing elit, sed do eiusmod tempoin cididunt ut labore et doloraliqua.</p>
    <div class="btn-outline" style="left:38px;top:476px;width:144px;height:46px">Read more</div>
  </article>

  <article class="card" style="left:609px;top:823px;width:241px;height:268px">
    <div class="photo" role="img" aria-label="Man in a grey suit relaxing on a city rooftop" style="height:171px;background:linear-gradient(160deg,#6c7278,#b7bcc0)"></div>
    <p class="mini-title" style="top:195px">Lorem ipsum dolotamet consectetur adipisin.</p>
  </article>
  <article class="card" style="left:881px;top:823px;width:241px;height:268px">
    <div class="photo" role="img" aria-label="Man jogging in a hooded top at sunrise" style="height:171px;background:linear-gradient(180deg,#d9c9a8,#8f8a66)"></div>
    <p class="mini-title" style="top:195px">Lorem ipsum dolotamet consectetur adipisin.</p>
  </article>
  <article class="card" style="left:609px;top:1123px;width:241px;height:268px">
    <div class="photo" role="img" aria-label="Two laughing friends in winter jackets" style="height:171px;background:linear-gradient(160deg,#8a8f8a,#6e4b3a)"></div>
    <p class="mini-title" style="top:195px">Lorem ipsum dolotamet consectetur adipisin.</p>
  </article>
  <article class="card" style="left:881px;top:1123px;width:241px;height:268px">
    <div class="photo" role="img" aria-label="Hiker with an orange backpack looking over green hills" style="height:171px;background:linear-gradient(180deg,#9aa98a,#4f6b3a)"></div>
    <p class="mini-title" style="top:195px">Lorem ipsum dolotamet consectetur adipisin.</p>
  </article>
</section>

<!-- Featured -->
<section class="featured">
  <div class="abs" style="left:0;top:1492px;width:1200px;height:518px;background:var(--band)"></div>
  <div class="abs kicker" style="left:70px;top:1617px">Featured</div>
  <h2 class="abs headline" style="left:70px;top:1646px;width:440px;font-weight:400">Lorem ipsum dolor sit amet, consectetur adipiscing elit, sed do eiusmod tempo.</h2>
  <p class="abs lede" style="left:70px;top:1782px;width:360px">Lorem ipsum dolor sit amet, consectetur adi pisc ing elit, sed do eiusmod tempo.</p>
  <div class="btn-outline" style="left:70px;top:1859px;width:144px;height:46px">Read more</div>
  <div class="photo" role="img" aria-label="Men in black capes getting haircuts in a dim barbershop" style="left:605px;top:1557px;width:544px;height:385px;background:linear-gradient(135deg,#3a3a36,#6a5a48 50%,#22272a)"></div>
</section>

<!-- Recent articles -->
<section class="recent">
  <h2 class="abs section-title" style="left:70px;top:2101px">Recent articles</h2>
  <nav class="tabs" style="left:572px;top:2107px"><span>All</span><span>Fashion</span><span>Luxury Lifestyle</span><span>Health</span><span>Fitness</span></nav>
  <div class="rule" style="top:2158px"></div>

  <article class="card" style="left:70px;top:2208px;width:338px;height:485px">
    <div class="photo" role="img" aria-label="Two friends laughing with drinks on a city street" style="height:228px;background:linear-gradient(135deg,#6e7a84,#a08064)"></div>
    <h3 class="abs" style="left:27px;top:252px;width:290px;font:500 25px/27px var(--serif)">Lorem ipsum dolor sita met consectetur adiscinpo in cididunt ut labore.</h3>
    <p class="abs" style="left:27px;top:362px;width:290px;font:400 13px/22px var(--sans);color:var(--muted)">Lorem ipsum dolor sit amet, conse ctetur adipiscing elit, sed do eiusm od tempor incididunt ut labore et dolore magna aliqua.</p>
  </article>
  <article class="card" style="left:427px;top:2208px;width:338px;height:485px">
    <div class="photo" role="img" aria-label="Two climbers scaling a rock face against the sun" style="height:228px;background:linear-gradient(200deg,#e6dcc4,#8c7a5c 55%,#3f3a32)"></div>
    <h3 class="abs" style="left:27px;top:252px;width:290px;font:500 25px/27px var(--serif)">Lorem ipsum dolor sita met consectetur adiscinpo in cididunt ut labore.</h3>
    <p class="abs" style="left:27px;top:362px;width:290px;font:400 13px/22px var(--sans);color:var(--muted)">Lorem ipsum dolor sit amet, conse ctetur adipiscing elit, sed do eiusm od tempor incididunt ut labore et dolore magna aliqua.</p>
  </article>
  <article class="card" style="left:784px;top:2208px;width:338px;height:485px">
    <div class="photo" role="img" aria-label="Man in a red jacket leaning against a brick wall" style="height:228px;background:linear-gradient(90deg,#e9e8e4,#8c2a2e 50%,#9a6a50)"></div>
    <h3 class="abs" style="left:27px;top:252px;width:290px;font:500 25px/27px var(--serif)">Lorem ipsum dolor sita met consectetur adiscinpo in cididunt ut labore.</h3>
    <p class="abs" style="left:27px;top:362px;width:290px;font:400 13px/22px var(--sans);color:var(--muted)">Lorem ipsum dolor sit amet, conse ctetur adipiscing elit, sed do eiusm od tempor incididunt ut labore et dolore magna aliqua.</p>
  </article>

  <div class="btn-solid" style="left:500px;top:2744px;width:200px;height:48px">View all articles</div>
</section>

<!-- Products -->
<section class="products">
  <div class="abs" style="left:0;top:2861px;width:1200px;height:621px;background:var(--band)"></div>
  <h2 class="abs section-title" style="left:0;width:1200px;text-align:center;top:2982px">Our products</h2>
  <svg class="abs" style="left:22px;top:3122px" width="16" height="28" viewBox="0 0 16 28" fill="none" stroke="#111" stroke-width="2.5"><polyline points="14,2 2,14 14,26"/></svg>
  <svg class="abs" style="left:1143px;top:3122px" width="16" height="28" viewBox="0 0 16 28" fill="none" stroke="#111" stroke-width="2.5"><polyline points="2,2 14,14 2,26"/></svg>

  <div class="photo" role="img" aria-label="Gin cocktails in coupe glasses with citrus" style="left:70px;top:3038px;width:196px;height:204px;background:linear-gradient(160deg,#3a3128,#c9b48a 60%,#e3d9b0)"></div>
  <div class="photo" role="img" aria-label="Whiskey bottle and glass on a dark table" style="left:284px;top:3038px;width:196px;height:204px;background:linear-gradient(160deg,#2a1e17,#7a4020 55%,#c0701e)"></div>
  <div class="photo" role="img" aria-label="Shaving brush, razor and shaving soap" style="left:498px;top:3038px;width:196px;height:204px;background:linear-gradient(160deg,#141414,#5a5148 55%,#8a2a2a)"></div>
  <div class="photo" role="img" aria-label="Tent and camping backpack in a forest" style="left:712px;top:3038px;width:196px;height:204px;background:linear-gradient(180deg,#4a5a60,#b87a3a 55%,#3a3a30)"></div>
  <div class="photo" role="img" aria-label="Loose pipe tobacco in a leather pouch" style="left:926px;top:3038px;width:196px;height:204px;background:linear-gradient(160deg,#3a2e28,#7a5234 55%,#a06a3c)"></div>

  <div class="product-label" style="left:70px;top:3264px">Gin</div>
  <div class="product-label" style="left:284px;top:3264px">Whiskey</div>
  <div class="product-label" style="left:498px;top:3264px">Barber<br>products</div>
  <div class="product-label" style="left:712px;top:3264px">Outdoor<br>equipment</div>
  <div class="product-label" style="left:926px;top:3264px">Tobacco</div>

  <div class="btn-solid" style="left:488px;top:3359px;width:222px;height:48px">Shop our products</div>
</section>

<!-- Recommended -->
<section class="recommended">
  <h2 class="abs section-title" style="left:70px;top:3553px">Recommended for you</h2>

  <div class="photo" role="img" aria-label="Grey-haired man in a denim jacket laughing in a forest" style="left:70px;top:3621px;width:338px;height:210px;background:linear-gradient(135deg,#6a6248,#3c5270 60%,#8a8a70)"></div>
  <div class="photo" role="img" aria-label="Two friends running together in a park" style="left:427px;top:3621px;width:338px;height:210px;background:linear-gradient(135deg,#8a9a6a,#8a2e30 55%,#c8c8c0)"></div>
  <div class="photo" role="img" aria-label="Friends toasting with glasses of beer" style="left:784px;top:3621px;width:338px;height:210px;background:linear-gradient(135deg,#3a2a20,#c07a2a 50%,#e8b070)"></div>
  <p class="rec-title" style="left:70px;top:3848px;width:340px">Lorem ipsum dolotametcons ectetur adipisin.</p>
  <p class="rec-title" style="left:427px;top:3848px;width:340px">Lorem ipsum dolotametcons ectetur adipisin.</p>
  <p class="rec-title" style="left:784px;top:3848px;width:340px">Lorem ipsum dolotametcons ectetur adipisin.</p>

  <div class="photo" role="img" aria-label="Pouring coffee from a black kettle into a cup" style="left:70px;top:3956px;width:338px;height:210px;background:linear-gradient(135deg,#e8e6e0,#7a7672 55%,#2a2624)"></div>
  <div class="photo" role="img" aria-label="Group of friends sharing burgers and beer in a bar" style="left:427px;top:3956px;width:338px;height:210px;background:linear-gradient(135deg,#2e2420,#8a5a36 55%,#d09a5a)"></div>
  <div class="photo" role="img" aria-label="Barber trimming a man's beard with scissors" style="left:784px;top:3956px;width:338px;height:210px;background:linear-gradient(135deg,#1c1c1e,#5a4438 55%,#9a7660)"></div>
  <p class="rec-title" style="left:70px;top:4183px;width:340px">Lorem ipsum dolotametcons ectetur adipisin.</p>
  <p class="rec-title" style="left:427px;top:4183px;width:340px">Lorem ipsum dolotametcons ectetur adipisin.</p>
  <p class="rec-title" style="left:784px;top:4183px;width:340px">Lorem ipsum dolotametcons ectetur adipisin.</p>
</section>

<!-- Footer -->
<footer>
  <div class="photo" role="img" aria-label="Group of hikers with backpacks crossing a log bridge in a misty mountain valley" style="left:0;top:4359px;width:1200px;height:752px;background:linear-gradient(180deg,#9aa3a0 0%,#56625a 30%,#3a4638 60%,#1a1d1a 85%,#0a0a0a 100%)"></div>
  <h2 class="abs" style="left:684px;top:4507px;font:400 25px/1 var(--serif);color:#fff;text-transform:uppercase;letter-spacing:.5px">Subscribe to our newsletter</h2>
  <div class="field" style="top:4553px">Name:</div>
  <div class="field" style="top:4625px">Email:</div>
  <div class="btn-solid" style="left:673px;top:4696px;width:432px;height:54px;border:2px solid #fff;font-size:13px">Subscribe now</div>

  <div class="abs" style="left:70px;top:4936px;font:500 31px/1 var(--serif);color:#fff;letter-spacing:1px;text-transform:uppercase">Tallbrook</div>
  <nav class="footer-nav"><span>Fashion</span><span>Luxury lifestyle</span><span>Health</span><span>Fitness</span><span>Our products</span></nav>
  <div class="social" style="left:969px"></div>
  <div class="social" style="left:1009px"></div>
  <div class="social" style="left:1049px"></div>
  <div class="social" style="left:1089px"></div>
  <p class="abs" style="left:70px;top:5046px;font:400 13px/1 var(--sans);color:#fff">Copyright © 2025 All Rights are reserved.</p>
</footer>

</body>
</html>
```